Exclusive Sleek Crowns Invite that connects barbers

I am looking for a general invitation to join a secret club of people that shave their head. I want it the size of a business card that I can hand out to people I see on the street. I want it to feel like a special exclulisve invite to a club that only they can be apart of and want to tell their friends about.

Target Market(s)

35-60 male

Industry/Entity Type

Hair

Contact Information for Business Card

I want it to look like an invite to a secret club that only people that shave their head can be apart of... I will hand it out to people that I think fir our demographic.

Font styles to use
Serif

Colors

Designer to choose colors to be used in the design.

Requirements
Must have
• A feel of exclusivity
• website address (www.sleekcrowns.com)
• logo

```html
<!DOCTYPE html>
<html lang="en">
<head>
<meta charset="utf-8">
<title>Sleek Crowns – Business Card</title>
<link rel="stylesheet" href="https://fonts.googleapis.com/css2?family=Cormorant+Garamond:wght@500;600&display=swap">
<style>
  :root {
    --backdrop: #3a312d;
    --card: #0f0e0e;
    --card-edge: #1c1a19;
    --gold: #d9b98c;
    --rose: #e39a86;
    --text-soft: #b3ada8;
    --silver: #dcdcdc;
    --divider: #2c2a29;
  }
  * { margin: 0; padding: 0; box-sizing: border-box; }
  html, body {
    width: 1200px; height: 844px; overflow: hidden;
    background: var(--backdrop);
    font-family: "Cormorant Garamond", Georgia, serif;
  }
  .canvas {
    position: relative; width: 1200px; height: 844px;
    display: flex; align-items: center; justify-content: center; gap: 48px;
  }
  .card {
    width: 520px; height: 300px;
    background: var(--card);
    border: 1px solid var(--card-edge);
    box-shadow: 0 10px 30px rgba(0,0,0,.45);
    position: relative;
  }
  /* Front: brand + contact */
  .card-front { display: flex; }
  .brand-side {
    width: 270px; display: flex; flex-direction: column;
    align-items: center; justify-content: center; gap: 16px;
  }
  .brand-mark {
    width: 64px; height: 64px; border: 4px solid var(--silver); border-radius: 6px;
  }
  .brand-name {
    font-size: 26px; font-weight: 600; color: var(--silver); letter-spacing: 1px;
    white-space: nowrap;
  }
  .divider { width: 1px; background: var(--divider); margin: 40px 0; }
  .contact-side {
    padding: 58px 0 0 26px; color: var(--text-soft);
    font-size: 14.5px; font-weight: 500; line-height: 1.35;
    white-space: nowrap;
  }
  .person-name {
    font-size: 17px; font-weight: 600; letter-spacing: 1.5px; color: var(--gold);
  }
  .person-name .surname { color: var(--rose); }
  .person-role { margin-bottom: 6px; }
  .contact-list { list-style: none; }
  .contact-list li { display: flex; align-items: center; gap: 8px; }
  .contact-list svg { width: 10px; height: 10px; fill: var(--gold); flex: none; }
  .address { margin-top: 8px; }
  /* Back: centred brand */
  .card-back {
    display: flex; flex-direction: column; align-items: center; justify-content: center; gap: 22px;
  }
  .card-back .brand-mark { width: 84px; height: 84px; }
  .card-back .brand-name { font-size: 48px; letter-spacing: 1.5px; }
</style>
</head>
<body>
<main class="canvas">
  <section class="card card-front">
    <div class="brand-side">
      <div class="brand-mark"></div>
      <div class="brand-name">Sleek Crowns</div>
    </div>
    <div class="divider"></div>
    <div class="contact-side">
      <div class="person-name">MARCUS <span class="surname">HALE</span></div>
      <div class="person-role">Managing Director</div>
      <ul class="contact-list">
        <li><svg viewBox="0 0 10 10"><path d="M1 3h8v6H1z M0 2c2-2 8-2 10 0v2H8V3H2v1H0z"/></svg>044-987 654 321</li>
        <li><svg viewBox="0 0 10 10"><path d="M2.5 0h5v10h-5z M3.5 1v7h3V1z"/></svg>044-987 654 321</li>
        <li><svg viewBox="0 0 10 10"><path d="M0 2h10v6H0z M0 2l5 3.5L10 2" stroke="#0f0e0e" stroke-width=".8"/></svg>info@sleekcrowns.com</li>
        <li><svg viewBox="0 0 10 10"><circle cx="5" cy="5" r="5"/></svg>www.sleekcrowns.com</li>
      </ul>
      <div class="address">48 Crown Lane,<br>Riverside City, 204816.</div>
    </div>
  </section>

  <section class="card card-back">
    <div class="brand-mark"></div>
    <div class="brand-name">Sleek Crowns</div>
  </section>
</main>
</body>
</html>
```